Vexora Design Project

International Travel agent, need a vexora design. We romote family travel destinations, Malrow, Kelvane Studios, and cruises.

Travel

```html
<!DOCTYPE html>
<html lang="en">
<head>
<meta charset="utf-8">
<title>Wander Bright Trips – Vexora Profile Theme</title>
<link rel="stylesheet" href="https://fonts.googleapis.com/css2?family=Arimo:wght@400;700&family=PT+Sans+Narrow:wght@400;700&family=PT+Sans:wght@400;700&family=Tinos:ital@1&display=swap">
<style>
:root{
  --sky-deep:#2f9fe0;
  --sky-light:#bfe6f8;
  --haze:#eef8fd;
  --sea:#1fa3d2;
  --sea-light:#78d2e6;
  --sand:#efe0bb;
  --panel:#ffffff;
  --sidebar:#e3e7e9;
  --sidebar-line:#cfd5d8;
  --ink:#222222;
  --tweet-ink:#333333;
  --muted:#999999;
  --brand-blue:#0e4f9c;
  --rule:#e2e2e2;
}
*{box-sizing:border-box;margin:0;padding:0}
html,body{width:1200px;height:900px;overflow:hidden}
body{
  position:relative;
  font-family:"Arimo",Arial,sans-serif;
  color:var(--ink);
  background:linear-gradient(180deg,var(--sky-deep) 0%,var(--sky-light) 30%,var(--haze) 46%,var(--sea-light) 52%,var(--sea) 62%,var(--sea-light) 76%,var(--sand) 86%,var(--sand) 100%);
}
.art{position:absolute}
.art--airliner{left:905px;top:105px;width:235px;height:120px;background:linear-gradient(160deg,#e6ebf0,#9aabb9)}
.art--landmarks{left:0;top:540px;width:314px;height:360px;background:linear-gradient(180deg,#9fc3d3 0%,#7fae6a 55%,#6f7a70 100%)}
.art--photo{position:absolute;background:#fff;padding:8px;box-shadow:0 4px 10px rgba(0,0,0,.3)}
.art--photo span{display:block;width:100%;height:100%}
.art--photo-pool{left:930px;top:555px;width:230px;height:170px;transform:rotate(-6deg)}
.art--photo-pool span{background:linear-gradient(160deg,#4aa9d8,#1f7fb5 60%,#d9b48a)}
.art--photo-family{left:955px;top:690px;width:220px;height:150px;transform:rotate(4deg)}
.art--photo-family span{background:linear-gradient(180deg,#8fd3f0,#2f8fc6 55%,#c79a72)}

.brand{position:absolute;left:30px;top:220px;display:flex;align-items:center;gap:10px}
.brand__dot{width:30px;height:30px;border-radius:50%;background:var(--brand-blue)}
.brand__name{font-family:"PT Sans",sans-serif;font-weight:700;font-size:26px;color:var(--brand-blue)}

.contact{position:absolute;left:54px;top:324px;font-family:"PT Sans Narrow",sans-serif;color:#000}
.contact__title{font-size:22px;margin-bottom:8px}
.contact__title b{font-weight:700}
.contact__name,.contact__phone{font-weight:700;font-size:16px;line-height:19px}
.contact__links{margin-top:12px;font-size:14px;line-height:16px;font-weight:700}

.topnav{position:absolute;left:624px;top:8px;width:261px;height:22px;background:#fff;border-radius:5px;display:flex;justify-content:space-around;align-items:center;font-size:10.5px;color:var(--ink)}

.profile{position:absolute;left:314px;top:52px;width:571px;height:848px;display:flex;border-radius:4px 4px 0 0;overflow:hidden}
.timeline{width:421px;background:var(--panel);padding:18px 18px 0 18px}
.sidebar{width:150px;background:var(--sidebar);border-left:1px solid var(--sidebar-line)}

.identity{display:flex;align-items:center;gap:14px;height:56px}
.identity__avatar{width:52px;height:44px;display:flex;align-items:center;justify-content:center}
.identity__avatar span{width:34px;height:34px;border-radius:50%;background:var(--brand-blue)}
.identity__handle{font-size:27px;font-weight:700;color:#333}

.featured{margin-top:44px;width:310px;font-size:19.5px;line-height:22px;color:var(--tweet-ink);padding-bottom:16px}
.meta{display:block;font-family:"Tinos",Georgia,serif;font-style:italic;font-size:8px;color:var(--muted);margin-top:4px;line-height:10px}
.featured .meta{margin-top:6px}

.stream{list-style:none;border-top:1px solid var(--rule)}
.tweet{font-size:11px;line-height:13px;color:var(--tweet-ink);padding:8px 80px 7px 4px;border-bottom:1px dashed var(--rule);position:relative}
.tweet__star{position:absolute;right:6px;top:9px;width:11px;height:11px}

.bio{padding:10px 10px 8px;font-size:9px;line-height:14px;color:#333}
.bio b{font-weight:700}
.stats{display:flex;gap:12px;padding:6px 10px 10px;border-bottom:1px solid var(--sidebar-line)}
.stats__item{font-size:11px;line-height:11px;color:#333}
.stats__item small{display:block;font-size:8px;color:#666;margin-top:2px}
.tab{font-size:11px;font-weight:700;padding:10px;border-bottom:1px solid var(--sidebar-line);color:#444}
.tab--active{background:#fff;color:#222}
.following{padding:10px}
.following__title{font-size:11px;font-weight:700;color:#444;margin-bottom:8px}
.following__grid{display:grid;grid-template-columns:repeat(6,19px);gap:3px}
.following__grid span{width:19px;height:19px;background:#fff;border:1px solid #d5d9db}
.rss{display:flex;align-items:center;gap:5px;padding:10px;font-size:8px;color:#444;border-top:1px solid var(--sidebar-line)}
.rss i{width:9px;height:9px;background:#9aa3a8;border-radius:2px}
</style>
</head>
<body>

<div class="art art--airliner" role="img" aria-label="Illustration of a passenger airliner flying"></div>
<div class="art art--landmarks" role="img" aria-label="Illustration of world landmarks with a road and greenery"></div>
<div class="art--photo art--photo-pool"><span role="img" aria-label="Photo of children playing in a water park"></span></div>
<div class="art--photo art--photo-family"><span role="img" aria-label="Photo of a family in a swimming pool"></span></div>

<div class="brand"><span class="brand__dot"></span><span class="brand__name">Wander Bright Trips</span></div>

<div class="contact">
  <p class="contact__title">Travel <b>Bright</b> and <b>Trips</b></p>
  <p class="contact__name">Tomas Ferreira</p>
  <p class="contact__phone">4519082</p>
  <p class="contact__links">Wanderbrighttrips.com<br>Wanderbrighttrips.presswell.com<br>Circlebook WanderBrightTrips</p>
</div>

<nav class="topnav"><span>Home</span><span>Profile</span><span>Find People</span><span>Settings</span><span>Help</span><span>Sign out</span></nav>

<main class="profile">
  <section class="timeline">
    <header class="identity">
      <div class="identity__avatar"><span></span></div>
      <h1 class="identity__handle">yourname</h1>
    </header>
    <p class="featured">New Blog post Free and Exclusive High Resolution Floral Close-ups http://lnkshrt.com/bg2hb9
      <span class="meta">5:04 PM Mar 2nd from Vx4me for Presswell</span></p>
    <ul class="stream">
      <li class="tweet">Cool app to convert pdf to word. http://lnkshrt.com/dxktcz<span class="meta">6:44 PM Feb 28th from web</span>
        <svg class="tweet__star" viewBox="0 0 10 10"><polygon points="5,0 6.2,3.6 10,3.7 7,6 8.1,9.6 5,7.5 1.9,9.6 3,6 0,3.7 3.8,3.6" fill="#aaa"/></svg></li>
      <li class="tweet">New Blog post Dingbats Anyone? http://lnkshrt.com/c4cy8n<span class="meta">6:45 PM Feb 27th from Vx4me for Presswell</span></li>
      <li class="tweet">New Blog post Best Bang for the Buck Recession Cars http://lnkshrt.com/d6ighj<span class="meta">5:04 PM Feb 27th from Vx4me for Presswell</span></li>
      <li class="tweet">New Blog post GFDR Nominated Best Presswell Themes and How to Pick the Right Theme For Your Blog http://lnkshrt.com/bk3a6a<span class="meta">2:25 PM Feb 27th from Vx4me for Presswell</span></li>
      <li class="tweet">New Blog post How to Use Layforge Separations Preview http://lnkshrt.com/bdczoe<span class="meta">4:55 PM Feb 26th from Vx4me for Presswell</span></li>
      <li class="tweet">New Blog post Latest on Orbis 7: Coming Out as Soon as September http://lnkshrt.com/c7bgzs<span class="meta">4:53 PM Feb 26th from Vx4me for Presswell</span></li>
      <li class="tweet">New Blog post Norvik asks Employees to Lay Themselves Off http://lnkshrt.com/brlbme<span class="meta">4:36 PM Feb 25th from Vx4me for Presswell</span></li>
      <li class="tweet">New Blog post 10 Essential Digital Camera Buying Tips http://lnkshrt.com/aresev<span class="meta">5:32 PM Feb 25th from Vx4me for Presswell</span></li>
      <li class="tweet">New Blog post Free 3d models: High-poly 3d Trees and Plants http://lnkshrt.com/a9zzv6<span class="meta">5:19 PM Feb 25th from Vx4me for Presswell</span></li>
    </ul>
  </section>

  <aside class="sidebar">
    <div class="bio">
      <p><b>Name</b> Your Name</p>
      <p><b>Location</b> Somewhere</p>
      <p><b>Web</b> http://www.qm.sg/</p>
      <p><b>Bio</b> Lorem Ipsum sit dolor. Blah blah blah.</p>
    </div>
    <div class="stats">
      <p class="stats__item">1,800<small>following</small></p>
      <p class="stats__item">1,876<small>followers</small></p>
      <p class="stats__item">250<small>updates</small></p>
    </div>
    <p class="tab tab--active">Updates</p>
    <p class="tab">Favorites</p>
    <div class="following">
      <p class="following__title">Following</p>
      <div class="following__grid">
        <span></span><span></span><span></span><span></span><span></span><span></span>
        <span></span><span></span><span></span><span></span><span></span><span></span>
        <span></span><span></span><span></span><span></span><span></span><span></span>
        <span></span><span></span><span></span><span></span><span></span><span></span>
        <span></span><span></span><span></span><span></span><span></span><span></span>
        <span></span><span></span><span></span>
      </div>
    </div>
    <p class="rss"><i></i>RSS feed</p>
  </aside>
</main>

</body>
</html>
```